New Website for Belcourt Manor at www.belcourt.com.au

A new logo has been designed (through pixel forge) and we now want to align the look and feel of our website at www.belcourt.com.au to the new logo. The content and page names (e.g. Grounds) will remain largely unchanged for the new site, so please submit a new look "Home" page, using our new logo, current text and any photos you choose from the existing gallery at our website. I have also attached the current "Home" page photos.

Industry/Entity Type

Accommodation

Number of Pages Required

1 page

Requirements
Must have
• Logo to be presented on white background.

```html
<!DOCTYPE html>
<html lang="en">
<head>
<meta charset="utf-8">
<title>Belcourt Manor – Home</title>
<link href="https://fonts.googleapis.com/css2?family=Open+Sans:wght@400;600;700;800&family=Noto+Serif:ital@1&display=swap" rel="stylesheet">
<style>
:root{
  --blue:#1f6fbf;
  --blue-dark:#175a9e;
  --teal:#1bb8c4;
  --ink:#222;
  --text:#444;
  --muted:#8a8a8a;
  --rule:#d8d8d8;
  --topbar:#f2f2f2;
  --header:#f7f7f7;
  --footer:#efefef;
  --white:#fff;
}
*{box-sizing:border-box;margin:0;padding:0}
html,body{width:1200px;height:2609px;overflow:hidden}
body{position:relative;background:var(--white);font-family:"Open Sans",Arial,sans-serif;color:var(--text)}
.abs{position:absolute}

.topbar{left:0;top:0;width:1200px;height:35px;background:var(--topbar);font-size:11px;color:var(--muted)}
.topbar span{position:absolute;top:11px}
.topbar .login b{color:var(--blue);font-weight:600}
.topbar .social{position:absolute;top:12px;width:10px;height:10px;border-radius:50%;background:#a8a8a8}

.header{left:0;top:35px;width:1200px;height:143px;background:var(--header)}
.logo{left:143px;top:9px;width:263px;height:125px;background:var(--white);display:flex;align-items:center;justify-content:center}
.logo .name{font-size:26px;font-weight:700;color:var(--blue)}
.contact{top:20px;font-size:11px;color:var(--ink);line-height:20px}
.contact .label{color:var(--muted);font-size:10px}
.contact-icon{top:30px;width:34px;height:34px;border-radius:50%;border:1.5px solid var(--blue);display:flex;align-items:center;justify-content:center}
.nav{left:459px;top:91px;width:741px;height:52px;background:var(--blue);display:flex;align-items:center;padding-left:34px}
.nav a{color:var(--white);font-size:11px;font-weight:700;text-decoration:none;margin-right:29px;text-transform:uppercase}
.nav a.active{border-bottom:1px solid var(--white);padding-bottom:3px;font-weight:600}
.nav .menu{position:absolute;right:6px;top:6px;width:38px;height:38px;background:var(--blue-dark);display:flex;flex-direction:column;justify-content:center;align-items:center;gap:4px}
.nav .menu i{display:block;width:16px;height:2px;background:var(--white)}

.hero{left:0;top:178px;width:1200px;height:516px;background:linear-gradient(180deg,#5f7d4a 0%,#d8643f 35%,#e8c970 58%,#a39a8c 82%,#5c6a44 100%)}
.hero h1{position:absolute;left:0;right:0;top:200px;text-align:center;color:var(--white);font-size:42px;font-weight:800;line-height:52px;text-shadow:0 2px 6px rgba(0,0,0,.4)}
.hero .arrow{position:absolute;top:215px;width:56px;height:56px;display:flex;align-items:center;justify-content:center;background:rgba(0,0,0,.3)}

.badge{width:48px;height:48px;border-radius:50%;background:var(--teal);border:4px solid #b7ecef;display:flex;align-items:center;justify-content:center;transform:translate(-50%,-50%);left:600px;z-index:2}

.kicker{left:0;width:1200px;text-align:center;font-family:"Noto Serif",Georgia,serif;font-style:italic;color:var(--muted)}
.title{left:0;width:1200px;text-align:center;font-size:22px;color:var(--ink);font-weight:400}
.title b{font-weight:700}
.rule{left:480px;width:240px;height:1px;background:var(--rule)}
.rule::after{content:"";position:absolute;left:90px;top:-1px;width:60px;height:3px;background:var(--blue)}

.desc{left:0;top:848px;width:1200px;text-align:center;font-size:12px;color:var(--ink);line-height:27px}

.stat{top:1002px;width:180px;margin-left:-90px;text-align:center}
.stat .ring{width:96px;height:96px;margin:0 auto;border-radius:50%;border:2px solid var(--blue);display:flex;align-items:center;justify-content:center}
.stat .label{margin-top:20px;font-family:"Noto Serif",Georgia,serif;font-style:italic;font-size:14px;color:var(--muted)}
.stat .num{font-size:30px;font-weight:700;color:var(--ink);line-height:34px}

.mansion{left:0;top:1237px;width:1200px;height:444px;background:linear-gradient(90deg,#2a2b2d,#141618 50%,#25313a)}
.mansion .photo{position:absolute;left:152px;top:54px;width:403px;height:334px;background:linear-gradient(160deg,#3f6a2e,#6e8f46 40%,#3aa6c8 60%,#2f5224)}
.mansion h2{position:absolute;left:600px;top:56px;font-size:22px;color:var(--white);font-weight:400}
.mansion h2 b{font-weight:700}
.mansion .line{position:absolute;left:600px;top:110px;width:150px;height:2px;background:var(--blue)}
.mansion .lead{position:absolute;left:600px;top:136px;font-size:11px;font-weight:700;color:var(--white)}
.mansion .item{position:absolute;left:600px;display:flex;gap:18px;color:#ddd;font-size:11px;line-height:17px;width:460px}
.mansion .item em{font-family:"Noto Serif",Georgia,serif;font-size:28px;color:#bbb;line-height:28px;min-width:24px}
.mansion .btn{position:absolute;left:600px;top:357px;width:92px;height:32px;background:var(--blue);color:var(--white);font-size:10px;font-weight:700;display:flex;align-items:center;justify-content:center;letter-spacing:.5px}

.filters{left:218px;top:1905px;display:flex;gap:38px}
.filters span{height:26px;border:1px solid #bbb;font-size:10px;font-weight:700;letter-spacing:1px;color:var(--ink);display:flex;align-items:center;justify-content:center;box-shadow:0 1px 2px rgba(0,0,0,.15)}
.count{left:230px;top:1866px;width:24px;height:24px;border-radius:50%;border:1.5px solid #e66;color:#e66;font-size:10px;display:flex;align-items:center;justify-content:center}
.grid{left:152px;top:1967px;width:896px;display:grid;grid-template-columns:repeat(3,295px);grid-auto-rows:204px;gap:6px}
.grid div{position:relative}
.grid .feature{background:rgba(31,111,191,.92);color:var(--white);text-align:center}
.grid .feature h3{margin-top:52px;font-size:20px;font-weight:400}
.grid .feature h3 b{font-weight:700}
.grid .feature p{font-family:"Noto Serif",Georgia,serif;font-style:italic;font-size:11px;margin-top:4px}
.grid .feature .plus{width:44px;height:44px;border-radius:50%;background:var(--white);color:var(--blue);margin:26px auto 0;font-size:24px;line-height:42px}

.newsletter{left:459px;top:2425px;width:741px;height:72px;background:var(--blue);display:flex;align-items:center;padding-left:26px;color:var(--white);font-size:14px}
.newsletter b{font-weight:700;margin-right:4px}
.newsletter .field{margin-left:40px;width:290px;height:34px;border:1px solid #7fb0e0;font-size:11px;display:flex;align-items:center;padding-left:16px;color:#dce9f7}
.newsletter .go{margin-left:12px;width:110px;height:34px;background:var(--white);color:var(--blue);font-size:10px;font-weight:700;letter-spacing:1px;display:flex;align-items:center;justify-content:center}

.footer{left:0;top:2497px;width:1200px;height:112px;background:var(--footer);text-align:center}
.footer .sep{position:absolute;left:500px;top:17px;width:200px;height:1px;background:#d0d0d0}
.footer .links{position:absolute;left:0;right:0;top:48px;font-size:9px;font-weight:700;color:var(--ink);word-spacing:2px}
.footer .copy{position:absolute;left:0;right:0;top:84px;font-size:10px;color:var(--ink)}
</style>
</head>
<body>

<div class="abs topbar">
  <span style="left:152px">&#9742;&nbsp; Request call back</span>
  <span class="login" style="left:278px">&#128274;&nbsp; <b>Login</b> or <b>Register</b></span>
  <span style="left:500px">For prices, availability and guest reviews, <u>visit Holidaze</u>.</span>
  <i class="social" style="left:860px"></i><i class="social" style="left:922px"></i><i class="social" style="left:979px"></i><i class="social" style="left:1038px"></i>
</div>

<header class="abs header">
  <div class="abs logo"><span class="name">Belcourt Manor</span></div>

  <div class="abs contact-icon" style="left:495px"><svg width="16" height="12" viewBox="0 0 16 12"><rect x="1" y="1" width="14" height="10" fill="none" stroke="#1f6fbf" stroke-width="1.5"/><path d="M4 5h8M4 8h5" stroke="#1f6fbf"/></svg></div>
  <div class="abs contact" style="left:549px"><div class="label">Fax</div>1300 555 010<br><span style="line-height:34px">www.belcourt.com.au</span></div>

  <div class="abs contact-icon" style="left:742px"><svg width="14" height="14" viewBox="0 0 14 14"><path d="M3 1l3 3-2 2c1 2 2 3 4 4l2-2 3 3-2 3C6 13 1 8 1 3z" fill="none" stroke="#1f6fbf" stroke-width="1.3"/></svg></div>
  <div class="abs contact" style="left:797px"><div class="label">Helen</div>0400 555 123<br><span style="line-height:34px">hb@belcourt.com.au</span></div>
  <div class="abs contact" style="left:948px"><div class="label">Martin</div>0400 555 456<br><span style="line-height:34px">mb@belcourt.com.au</span></div>

  <nav class="abs nav">
    <a class="active">Home</a><a>Mansion</a><a>Bedrooms</a><a>Owl &amp; Otter</a><a>Grounds</a><a>Gallery</a><a>DIY Weddings</a>
    <div class="menu"><i></i><i></i><i></i></div>
  </nav>
</header>

<section class="abs hero" role="img" aria-label="Aerial photo of the yellow manor house with terracotta roofs, gravel drive and palm gardens">
  <h1>PALATIAL ESTATE AND<br>LUXURY RESORT</h1>
  <div class="arrow" style="left:80px"><svg width="14" height="20"><path d="M11 2L3 10l8 8" stroke="#fff" stroke-width="2" fill="none"/></svg></div>
  <div class="arrow" style="left:1064px"><svg width="14" height="20"><path d="M3 2l8 8-8 8" stroke="#fff" stroke-width="2" fill="none"/></svg></div>
</section>

<div class="abs badge" style="top:694px"><svg width="22" height="20" viewBox="0 0 22 20"><path d="M11 1L1 10h3v9h5v-6h4v6h5v-9h3z" fill="#fff"/></svg></div>

<p class="abs kicker" style="top:738px;font-size:12px">A few words about the house</p>
<h2 class="abs title" style="top:762px"><b>Property</b> Description</h2>
<div class="abs rule" style="top:816px"></div>

<div class="abs desc">
  On over 2 manicured garden acres, Belcourt Manor is a unique Gold Coast estate, centrally located in the prestigious rural suburb of Linden Vale. <u>More about our Location</u><br>
  The estate features a grand mansion, private pub (The Owl and Otter), sparkling resort pool, tennis court and playground.<br>
  Magnificent properties rarely feel so warm and welcoming – so browse away and visit our <u>photo gallery</u> – and we look forward to having you stay as our guests.<br>
  For prices, availability and guest reviews, <u>visit Holidaze</u>.
</div>

<div class="abs stat" style="left:227px">
  <div class="ring"><svg width="40" height="40" viewBox="0 0 40 40" fill="none" stroke="#1f6fbf" stroke-width="2.5"><path d="M6 6h28v28H6z"/><path d="M14 22v6h6" stroke-width="3"/></svg></div>
  <div class="label">Square Feet</div><div class="num">2500</div>
</div>
<div class="abs stat" style="left:419px">
  <div class="ring"><svg width="44" height="36" viewBox="0 0 44 36" fill="none" stroke="#1f6fbf" stroke-width="2"><rect x="6" y="3" width="32" height="14" rx="2"/><rect x="11" y="8" width="9" height="6" rx="1"/><rect x="24" y="8" width="9" height="6" rx="1"/><rect x="2" y="17" width="40" height="10" rx="1"/><path d="M5 27v5M39 27v5"/></svg></div>
  <div class="label">Bedrooms</div><div class="num">3</div>
</div>
<div class="abs stat" style="left:610px">
  <div class="ring"><svg width="44" height="40" viewBox="0 0 44 40" fill="none" stroke="#1f6fbf" stroke-width="2"><path d="M4 22h36v4a9 9 0 0 1-9 9H13a9 9 0 0 1-9-9z"/><path d="M10 35l-2 4M34 35l2 4M30 22V6a3 3 0 0 1 6 0"/><path d="M22 12l8 4M24 8l2 3M20 15l2 3"/></svg></div>
  <div class="label">Bathrooms</div><div class="num">2</div>
</div>
<div class="abs stat" style="left:797px">
  <div class="ring"><svg width="46" height="44" viewBox="0 0 46 44" fill="none" stroke="#1f6fbf" stroke-width="2"><rect x="3" y="6" width="32" height="28" rx="2"/><path d="M3 13h32M10 3v6M28 3v6"/><path d="M9 19h3M16 19h3M23 19h3M9 25h3M16 25h3"/><circle cx="34" cy="32" r="9" fill="#fff"/><path d="M34 27v5h4"/></svg></div>
  <div class="label">Year Built</div><div class="num">2015</div>
</div>
<div class="abs stat" style="left:971px">
  <div class="ring"><svg width="44" height="40" viewBox="0 0 44 40" fill="#1f6fbf"><circle cx="12" cy="8" r="5"/><rect x="17" y="7" width="14" height="3"/><path d="M6 20l4-7h24l4 7v12H6z"/><rect x="8" y="32" width="6" height="5"/><rect x="30" y="32" width="6" height="5"/><circle cx="12" cy="25" r="2.5" fill="#fff"/><circle cx="32" cy="25" r="2.5" fill="#fff"/></svg></div>
  <div class="label">Car Parking</div><div class="num">3</div>
</div>

<section class="abs mansion">
  <div class="photo" role="img" aria-label="Aerial photo of the mansion with swimming pool and tropical gardens"></div>
  <h2><b>Grand</b> Mansion</h2>
  <div class="line"></div>
  <div class="lead">You'll feel like royalty in a mansion with: -</div>
  <div class="item" style="top:164px"><em>1.</em><span style="padding-top:8px">Regal entrance and sweeping staircase.</span></div>
  <div class="item" style="top:219px"><em>2.</em><span style="padding-top:2px">Stately lounge or ballroom with 18 foot panelled ceiling and gas-driven fireplace – fondly referred to as "The Halloway Room".</span></div>
  <div class="item" style="top:280px"><em>3.</em><span style="padding-top:8px">Elegant formal dining room.</span></div>
  <div class="btn">LEARN MORE</div>
</section>

<div class="abs badge" style="top:1237px"><svg width="22" height="20" viewBox="0 0 22 20" fill="none" stroke="#fff" stroke-width="2"><path d="M11 2L2 10h3v8h12v-8h3z"/><rect x="9" y="12" width="4" height="6"/></svg></div>

<div class="abs badge" style="top:1681px"><svg width="22" height="20" viewBox="0 0 22 20" fill="none" stroke="#fff" stroke-width="2"><rect x="2" y="2" width="18" height="16"/><path d="M4 15l5-6 4 4 3-3 3 5"/></svg></div>

<h2 class="abs title" style="top:1719px"><b>Our</b> Gallery</h2>
<p class="abs kicker" style="top:1760px;font-size:13px;line-height:21px">You are welcome to check out our house gallery to make sure that this home<br>is in prime condition which makes it a perfect living space.</p>
<div class="abs rule" style="top:1822px"></div>

<div class="abs count">6</div>
<div class="abs filters">
  <span style="width:42px">ALL</span><span style="width:112px">LIVING ROOM</span><span style="width:112px">BASEMENT</span><span style="width:112px">BEDROOM</span><span style="width:104px">KITCHEN</span><span style="width:96px">GARAGE</span>
</div>

<div class="abs grid">
  <div role="img" aria-label="Covered veranda at dusk with lit dining room" style="background:linear-gradient(135deg,#2b4670,#c58a3c 60%,#6b4a2a)"></div>
  <div role="img" aria-label="Garden lawn event with dark car parked under trees" style="background:linear-gradient(160deg,#5f8a3a,#9fb56a 45%,#2a2c30)"></div>
  <div class="feature" role="img" aria-label="Gallery album cover over interior photo">
    <h3><b>Our</b> Gallery</h3><p>December 22nd, 2015</p><div class="plus">+</div>
  </div>
  <div role="img" aria-label="Upstairs hallway with arched doorways and balustrade" style="background:linear-gradient(150deg,#e8d9b8,#c9a77c 50%,#8f6b45)"></div>
  <div role="img" aria-label="Dining hall with guests seated at long tables" style="background:linear-gradient(170deg,#d9c48a,#8a5a3a 55%,#4a3328)"></div>
  <div role="img" aria-label="Curved entrance staircase with blue carpet" style="background:linear-gradient(140deg,#efe6d4,#c49a66 50%,#5b8fb0)"></div>
</div>

<div class="abs newsletter"><b>Submit</b> Newsletter<div class="field">Email ID</div><div class="go">SUBSCRIBE</div></div>

<footer class="abs footer">
  <div class="sep"></div>
  <div class="links">HOME &nbsp;| &nbsp;MANSION &nbsp;| &nbsp;BEDROOMS &nbsp;| &nbsp;OPTIONS &nbsp;| &nbsp;OWL AND OTTER &nbsp;| &nbsp;GROUNDS &nbsp;| &nbsp;LOCATION &nbsp;| &nbsp;GALLERY &nbsp;| &nbsp;CONTACT &nbsp;| &nbsp;AVAILABILITY &nbsp;| &nbsp;DIY WEDDINGS</div>
  <div class="copy">© 2016 <b>Belcourt Manor</b> | All rights reserved</div>
</footer>

</body>
</html>
```